Business Card Design

We are a manufacturing and distribution company with most of our customer base being supermarkets. We have established brand guidelines that are attached.

```html
<!DOCTYPE html>
<html lang="en">
<head>
<meta charset="utf-8">
<title>Korvane Business Card</title>
<link rel="stylesheet" href="https://fonts.googleapis.com/css2?family=Arimo:wght@400;700&display=swap">
<style>
  :root {
    --page-bg: #e4e4e4;
    --card-dark: #232122;
    --card-dark-shape: #2f2d2e;
    --card-light: #ffffff;
    --brand-red: #d7141c;
    --brand-blue: #0065a8;
    --ink: #1c1a1b;
    --ink-light: #f2f2f2;
  }
  * { margin: 0; padding: 0; box-sizing: border-box; }
  html, body { width: 1200px; height: 802px; overflow: hidden; }
  body {
    background: var(--page-bg);
    font-family: "Arimo", Arial, sans-serif;
    position: relative;
  }
  .card {
    position: absolute;
    top: 252px;
    width: 520px;
    height: 298px;
    overflow: hidden;
    border-bottom: 3px solid var(--brand-red);
    border-left: 2px solid var(--brand-red);
    box-shadow: 0 8px 20px rgba(0,0,0,0.18);
  }
  .card--front { left: 50px; background: var(--card-dark); color: var(--ink-light); }
  .card--back { left: 630px; background: var(--card-light); color: var(--ink); }

  .decor-square { position: absolute; }
  .card--front .decor-square {
    right: -40px; top: -60px; width: 230px; height: 230px;
    background: var(--card-dark-shape); border-radius: 8px;
  }
  .card--back .decor-square {
    left: -70px; bottom: -70px; width: 230px; height: 230px;
    background: var(--brand-blue); border-radius: 8px;
  }

  .brand { position: absolute; display: flex; align-items: center; gap: 10px; }
  .brand-mark { width: 16px; height: 16px; background: var(--brand-red); }
  .brand-name { font-weight: 700; letter-spacing: 1px; }
  .card--front .brand { left: 42px; top: 62px; }
  .card--front .brand-name { font-size: 26px; color: var(--ink-light); }
  .card--back .brand { left: 210px; top: 128px; }
  .card--back .brand-name { font-size: 32px; color: var(--ink); }
  .card--back .brand-mark { width: 22px; height: 22px; }

  .person { position: absolute; left: 68px; top: 112px; }
  .person-name { color: var(--brand-red); font-size: 15px; letter-spacing: 0.5px; }
  .person-role { font-size: 13px; margin-top: 2px; }

  .address { position: absolute; left: 68px; top: 160px; font-size: 13px; line-height: 1.25; }

  .contacts { position: absolute; left: 68px; top: 204px; list-style: none; font-size: 13px; }
  .contacts li { display: flex; align-items: center; gap: 10px; line-height: 1.5; }
  .contacts svg { width: 11px; height: 11px; flex: none; }
</style>
</head>
<body>
  <section class="card card--front">
    <div class="decor-square" role="img" aria-label="Faint brand shape decoration"></div>
    <div class="brand">
      <span class="brand-mark"></span>
      <span class="brand-name">KORVANE</span>
    </div>
    <div class="person">
      <p class="person-name">DANIEL PORTER</p>
      <p class="person-role">Manager</p>
    </div>
    <p class="address">Your address, city<br>state, ZIP 0000</p>
    <ul class="contacts">
      <li>
        <svg viewBox="0 0 12 12" aria-hidden="true"><path fill="var(--brand-red)" d="M2.5 0.5l2 2.4-1.2 1.3c.7 1.6 2 2.9 3.5 3.6l1.3-1.2 2.4 2-1.2 2C4.7 10.2 1.6 7 .6 2z"/></svg>
        <span>555-318-2740</span>
      </li>
      <li>
        <svg viewBox="0 0 12 12" aria-hidden="true"><rect x="0.8" y="2.3" width="10.4" height="7.4" fill="none" stroke="var(--brand-red)" stroke-width="1.3"/><path d="M1 2.6l5 4 5-4" fill="none" stroke="var(--brand-red)" stroke-width="1.3"/></svg>
        <span>hello@korvane.com</span>
      </li>
      <li>
        <svg viewBox="0 0 12 12" aria-hidden="true"><circle cx="6" cy="6" r="5.2" fill="none" stroke="var(--brand-red)" stroke-width="1.2"/><path d="M0.8 6h10.4M6 0.8c-2.6 3-2.6 7.4 0 10.4M6 0.8c2.6 3 2.6 7.4 0 10.4" fill="none" stroke="var(--brand-red)" stroke-width="1"/></svg>
        <span>www.korvane.com</span>
      </li>
    </ul>
  </section>

  <section class="card card--back">
    <div class="decor-square" role="img" aria-label="Blue brand shape decoration"></div>
    <div class="brand">
      <span class="brand-mark"></span>
      <span class="brand-name">KORVANE</span>
    </div>
  </section>
</body>
</html>
```